Shopify Design for Back Pain Patch

We need a design for the Shopify-based homepage of the new Vortilo Spine Patch.

The Vortilo spine patch absorbs the surface energy produced by your body when you are in pain and redistributes it, reducing your discomfort. It is approximately 5” x 5” in size, with an adhesive backing on one side and a cloth-like exterior that is neutral/light tan in color.

We need a website design that matches our packaging (see attached assets). This includes the blue/orange color scheme and our key messages:

-Natural relief for back pain
-Soothes using your body's natural energy
-Odorless, Gentle, Easy to Use
-Reusable up to 5 days

We are going to be using the Shopify platform for this website, so we'd like the design to be usable with this theme:
http://pliantframe.examplestore.net/pages/theme-features

We will do all of the coding, but please keep this layout in mind for the design.

Target Market(s)

The Vortilo Spine Patch is targeted to people suffering from mild to moderate, chronic back pain, but who desire to continue leading active lives.

Industry/Entity Type

Adhesive

Requirements
Must have
• The design needs to have the same look and feel as the packaging for the back patch. Please feel free to use any of the attached assets in your design (doesn't need to be all).
Should not have
• We do not want to see stock photography other than the assets provided.

```html
<!DOCTYPE html>
<html lang="en">
<head>
<meta charset="utf-8">
<title>Vortilo Spine Patch</title>
<link rel="stylesheet" href="https://fonts.googleapis.com/css2?family=Oswald:wght@400;500&family=Questrial&family=Open+Sans:wght@400;600;700&display=swap">
<style>
:root{
  --orange:#f07a20;
  --orange-deep:#e2661a;
  --blue:#1c64b8;
  --blue-deep:#1b3f95;
  --navy:#2b3888;
  --red:#c8321e;
  --text:#333;
  --footer:#f1f1f1;
}
*{margin:0;padding:0;box-sizing:border-box}
html,body{width:1200px;height:1029px;overflow:hidden;background:#fff}
body{position:relative;font-family:"Open Sans",sans-serif;color:var(--text)}
.abs{position:absolute}
.hero-art{position:absolute;left:0;top:0;width:1200px;height:588px}

.main-nav{left:200px;top:17px;height:28px;display:flex;align-items:center;font-family:"Oswald",sans-serif;font-size:15px;color:#fff;letter-spacing:.5px}
.main-nav a{color:#fff;text-decoration:none;text-shadow:0 1px 1px rgba(0,0,0,.25)}
.main-nav .current{background:var(--blue);border:1px solid #fff;border-radius:14px;padding:3px 16px}
.main-nav .about{margin-left:30px}.main-nav .products{margin-left:43px}.main-nav .blog{margin-left:39px}.main-nav .contact{margin-left:43px}
.utility{top:25px;font-family:"Open Sans",sans-serif;font-weight:700;font-size:10.5px;color:#fff;letter-spacing:-.2px}
.utility.phone{left:750px}.utility.login{left:928px}

.brand{left:248px;top:98px;font-family:"Questrial",sans-serif;color:var(--orange);line-height:1}
.brand .name{font-size:62px;letter-spacing:-1px}
.brand .sub{font-size:23px;margin:6px 0 0 66px}

.tagline{left:210px;top:235px;font-family:"Questrial",sans-serif;font-size:27px;color:var(--blue)}
.benefit{left:214px;width:292px;height:45px;border-radius:0 10px 10px 0;background:linear-gradient(90deg,rgba(28,100,184,0) 0%,rgba(28,100,184,.85) 22%,var(--blue) 45%);font-family:"Oswald",sans-serif;font-size:29px;color:#fff;text-align:center;line-height:45px;padding-left:22px}
.reusable{left:249px;top:426px;width:252px;height:45px}
.reusable span{position:absolute;left:0;top:0;width:100%;text-align:center;line-height:45px;font-family:"Oswald",sans-serif;font-style:italic;font-size:20px;color:#fff}
.features{left:646px;top:430px;font-family:"Oswald",sans-serif;font-style:italic;font-size:22px;color:#fff;word-spacing:2px;text-shadow:0 1px 2px rgba(0,0,0,.2)}
.features b{font-weight:400;margin-right:18px}
.contents{left:804px;top:463px;font-size:10.5px;font-weight:600;color:#fff}
.slogan{left:0;width:1200px;text-align:center;font-family:"Questrial",sans-serif}
.slogan.top{top:486px;font-size:29px;color:#fff;letter-spacing:1px}
.slogan.bottom{top:515px;font-size:38px;color:var(--orange);letter-spacing:1.5px;font-weight:700}

.panel{left:176px;top:567px;width:848px;height:340px;background:#fff}
.section-title{font-family:"Questrial",sans-serif;font-size:21px;color:var(--navy);font-weight:700;letter-spacing:.3px}
.section-title .accent{color:var(--orange)}
.text-column{position:absolute}
.copy{font-size:10.5px;line-height:18px;letter-spacing:0}
.copy strong{font-weight:700;color:#222}
.readmore{display:block;margin-top:7px;font-size:10.8px;line-height:14px;color:var(--red);text-decoration:none}

.photo{border:4px solid #8c8c8c;outline:1px solid #ccc}
.social{left:663px;top:849px;display:flex;gap:3px}
.social span{width:31px;height:31px;border-radius:50%;background:#4f86d6;border:2px solid #c9dbf3;color:#fff;font-size:6.5px;display:flex;align-items:center;justify-content:center;font-weight:600}

.footer{left:0;top:900px;width:1200px;height:129px}
.copyright{left:200px;top:958px;font-size:10.8px;font-weight:600;color:#222}
.cards{left:197px;top:981px;display:flex;gap:4px;background:#fff;padding:3px;border:1px solid #eee}
.cards span{width:35px;height:20px;border:1px solid #ccc;font-size:7.5px;font-weight:700;display:flex;align-items:center;justify-content:center;color:var(--blue-deep)}
.footer-brand{left:810px;top:948px;font-family:"Questrial",sans-serif;color:var(--orange);line-height:1}
.footer-brand .name{font-size:46px;letter-spacing:-1px}
.footer-brand .sub{font-size:18px;margin:3px 0 0 48px}
</style>
</head>
<body>

<svg class="hero-art" viewBox="0 0 1200 588">
  <defs>
    <linearGradient id="sky" x1="0" y1="0" x2="0" y2="1">
      <stop offset="0" stop-color="#cfe0f0"/>
      <stop offset=".55" stop-color="#eaf2f9"/>
      <stop offset="1" stop-color="#9fb3c6"/>
    </linearGradient>
    <linearGradient id="orangeBand" x1="0" y1="0" x2="0" y2="1">
      <stop offset="0" stop-color="#f58a2a"/>
      <stop offset="1" stop-color="#ee6d17"/>
    </linearGradient>
    <linearGradient id="blueBand" x1="0" y1="0" x2="1" y2="0">
      <stop offset="0" stop-color="#1f4fa5"/>
      <stop offset=".5" stop-color="#1a3f92"/>
      <stop offset="1" stop-color="#2b5cb8"/>
    </linearGradient>
  </defs>
  <rect width="1200" height="588" fill="url(#orangeBand)"/>
  <path d="M0,60 Q400,30 1200,52" stroke="#f9a55c" stroke-width="14" fill="none" opacity=".35"/>
  <g role="img" aria-label="Photo of a cyclist in a red and white jersey wearing a tan patch on his lower back, city skyline behind">
    <path d="M0,103 Q500,40 1200,72 L1200,428 Q800,410 600,428 Q300,420 0,388 Z" fill="url(#sky)"/>
  </g>
  <path d="M0,400 Q400,420 700,440 T1200,470" stroke="#f9a55c" stroke-width="10" fill="none" opacity=".4"/>
  <path d="M0,470 Q500,440 1200,500" stroke="#f9a55c" stroke-width="6" fill="none" opacity=".35"/>
  <path d="M0,523 Q500,468 1200,500 L1200,588 L0,588 Z" fill="url(#blueBand)"/>
  <path d="M700,560 Q1000,520 1200,560" stroke="#4d7fd0" stroke-width="6" fill="none" opacity=".5"/>
  <path d="M950,588 Q1100,540 1200,545 L1200,588 Z" fill="#f07a20" opacity=".9"/>
</svg>

<nav class="abs main-nav">
  <a class="current" href="#">HOME</a>
  <a class="about" href="#">ABOUT</a>
  <a class="products" href="#">PRODUCTS</a>
  <a class="blog" href="#">BLOG</a>
  <a class="contact" href="#">CONTACT</a>
</nav>
<div class="abs utility phone">Questions? Call 1-800-555-0199</div>
<div class="abs utility login">Customer Login</div>

<div class="abs brand"><div class="name">Vortilo</div><div class="sub">Spine Patch</div></div>

<div class="abs tagline">Natural relief for back pain</div>
<div class="abs benefit" style="top:277px">Sprains</div>
<div class="abs benefit" style="top:327px">Sore Muscles</div>
<div class="abs benefit" style="top:377px">Backache</div>

<div class="abs reusable">
  <svg width="252" height="45" viewBox="0 0 252 45"><path d="M18,2 L250,2 L234,43 L2,43 Z" fill="#e2661a" stroke="#fff" stroke-width="3"/></svg>
  <span>Reusable up to 5 days</span>
</div>

<div class="abs features"><b>• Odorless</b><b>• Gentle</b><b style="margin:0">• Easy to use</b></div>
<div class="abs contents">Contains 3 patches ( 4.75&nbsp; X 4.75 )</div>

<div class="abs slogan top">SOOTHES USING YOUR</div>
<div class="abs slogan bottom">BODY’S NATURAL ENERGY</div>

<div class="abs panel"></div>

<h2 class="abs section-title" style="left:201px;top:584px"><span class="accent">Vortilo</span> Spine Patch</h2>
<div class="text-column" style="left:200px;top:626px;width:207px">
  <p class="copy"><strong>Lorem ipsum dolor sit amet, consectetuer adipiscing elit, sed diam</strong> nonummy nibh euismod tincidunt ut laoreet dolore magna aliquam erat volutpat. Ut wisi enim ad minim veniam, quis nostrud exerci tation ullamcorper suscipit lobortis nisl ut aliquip ex ea commodo consequat. Duis autem vel eum iriure dolor in hendrerit in vulputate velit esse molestie consequat, vel illum dolore eu feugiat nulla facilisis at vero eros et accumsan et iusto odio dignissim qui blandit praesent luptatum zzril delenit augue duis dolore te feugait nulla facilisi.</p>
  <a class="readmore" href="#">» Readmore</a>
</div>
<div class="abs photo" role="img" aria-label="Photo of a runner stretching against a pole beside a park path, patch on her lower back" style="left:421px;top:626px;width:205px;height:267px;background:linear-gradient(180deg,#c9ccd0 0%,#9aa0a6 45%,#5a5f55 100%)"></div>

<h2 class="abs section-title" style="left:664px;top:584px">Our Products</h2>
<div class="abs photo" role="img" aria-label="Product box showing a bare back with patch outlines and the blue and orange package panel" style="left:663px;top:627px;width:134px;height:136px;border-width:2px;background:linear-gradient(90deg,#c98a62 0%,#e7b08b 50%,#2c5cb3 100%)"></div>
<div class="text-column" style="left:813px;top:626px;width:200px">
  <p class="copy">Lorem ipsum dolor sit amet, consectetuer adipiscing elit, sed diam nonummy nibh euismod tincidunt ut laoreet dolore magna aliquam erat volutpat. Ut wisi enim ad minim veniam, quis nostrud exerci tation ullamcorper suscipit lobortis nisl ut aliquip</p>
  <a class="readmore" href="#">» Readmore</a>
</div>

<h2 class="abs section-title" style="left:665px;top:812px;color:var(--orange)">Find Us At</h2>
<div class="abs social">
  <span>Frendo</span><span>Chirpa</span><span>Vidora</span><span>Linka</span><span>Tagly</span>
</div>

<svg class="abs footer" viewBox="0 0 1200 129" aria-hidden="true">
  <defs><linearGradient id="foot" x1="0" y1="0" x2="0" y2="1"><stop offset="0" stop-color="#fbfbfb"/><stop offset="1" stop-color="#ececec"/></linearGradient></defs>
  <path d="M0,13 Q600,45 1200,5 L1200,129 L0,129 Z" fill="url(#foot)"/>
  <path d="M0,13 Q600,45 1200,5" stroke="#d6d6d6" fill="none"/>
</svg>

<div class="abs copyright">Copyright © vortilo 2013</div>
<div class="abs cards">
  <span>Norda</span><span>Pellix</span><span>Amara</span><span>Quovi</span><span>Paylo</span>
</div>

<div class="abs footer-brand"><div class="name">Vortilo</div><div class="sub">Spine Patch</div></div>

</body>
</html>
```